Business cards for financial advisor-insurance agent firm

Our company, Harlow Pemberton Insurance & Investments, is an insurance (health, life, home, auto, etc) and investment brokerage offering a suite of options to meet client needs. We need business cards that are professional and embody strength, security and sophistication.

Also running a letterhead project at
http://jobs.briefmarlo.com/job.aspx?id=519087

Target Market(s)

Upper middle class and wealthy

Industry/Entity Type

Investment

Requirements
Nice to have
• Looking for either white, navy blue, or gray cards

```html
<!DOCTYPE html>
<html lang="en">
<head>
<meta charset="utf-8">
<title>Harlow Pemberton Insurance &amp; Investments — Business Card</title>
<link rel="stylesheet" href="https://fonts.googleapis.com/css2?family=Cinzel:wght@400;500&family=Open+Sans:wght@300;400&display=swap">
<style>
  :root {
    --backdrop: #c9c9c7;
    --card-paper: #f4f4f2;
    --navy: #1f2a5a;
    --frame-line: #4a5a6a;
    --contact-grey: #8a8c90;
  }
  * { margin: 0; padding: 0; box-sizing: border-box; }
  html, body {
    width: 1200px;
    height: 728px;
    overflow: hidden;
    background: var(--backdrop);
  }
  .canvas {
    width: 1200px;
    height: 728px;
    display: flex;
    align-items: center;
    justify-content: center;
  }
  .business-card {
    position: relative;
    width: 920px;
    height: 526px;
    background: var(--card-paper);
    box-shadow: 0 6px 18px rgba(0,0,0,0.18);
  }
  .card-frame {
    position: absolute;
    inset: 22px;
    border: 1.5px solid var(--frame-line);
  }
  .brand {
    position: absolute;
    left: 150px;
    top: 150px;
    display: flex;
    align-items: center;
    gap: 22px;
  }
  .brand-square {
    width: 78px;
    height: 78px;
    border: 3px solid var(--navy);
    flex-shrink: 0;
  }
  .brand-name {
    font-family: "Cinzel", serif;
    font-weight: 500;
    color: var(--navy);
    font-size: 40px;
    letter-spacing: 1px;
    line-height: 1;
  }
  .brand-tagline {
    font-family: "Cinzel", serif;
    font-weight: 400;
    color: var(--navy);
    font-size: 15px;
    letter-spacing: 1.5px;
    margin-top: 8px;
    text-align: right;
  }
  .contact-list {
    position: absolute;
    list-style: none;
    font-family: "Open Sans", sans-serif;
    font-weight: 300;
    font-size: 22px;
    color: var(--contact-grey);
  }
  .contact-list li {
    display: flex;
    align-items: center;
    gap: 16px;
    height: 44px;
  }
  .contact-icon { width: 20px; height: 20px; fill: var(--navy); flex-shrink: 0; }
  .contact-list--office { left: 70px; bottom: 60px; }
  .contact-list--online { right: 70px; top: 300px; }
</style>
</head>
<body>
<main class="canvas">
  <section class="business-card">
    <div class="card-frame"></div>

    <div class="brand">
      <div class="brand-square"></div>
      <div class="brand-text">
        <div class="brand-name">Harlow Pemberton</div>
        <div class="brand-tagline">Insurance &amp; Investments</div>
      </div>
    </div>

    <ul class="contact-list contact-list--office">
      <li>
        <svg class="contact-icon" viewBox="0 0 20 20" aria-hidden="true"><path d="M10 1a6.5 6.5 0 0 0-6.5 6.5C3.5 12.5 10 19 10 19s6.5-6.5 6.5-11.5A6.5 6.5 0 0 0 10 1zm0 9a2.5 2.5 0 1 1 0-5 2.5 2.5 0 0 1 0 5z"/></svg>
        <span>880 Marlowe Lane</span>
      </li>
      <li>
        <svg class="contact-icon" viewBox="0 0 20 20" aria-hidden="true"><path d="M2 6c0-2 2-3 8-3s8 1 8 3v2h-4V6.5c-1-.4-2.4-.5-4-.5s-3 .1-4 .5V8H2V6zm3 3h10l2 8H3l2-8zm5 2a2.5 2.5 0 1 0 0 5 2.5 2.5 0 0 0 0-5z"/></svg>
        <span>0198 765 432</span>
      </li>
    </ul>

    <ul class="contact-list contact-list--online">
      <li>
        <svg class="contact-icon" viewBox="0 0 20 20" aria-hidden="true"><path d="M1 4h18v12H1V4zm2 1.5 7 5.5 7-5.5H3zm-.5 1.5v8h15V7l-7.5 6-7.5-6z"/></svg>
        <span>office@harlowpemberton.com</span>
      </li>
      <li>
        <svg class="contact-icon" viewBox="0 0 20 20" aria-hidden="true"><circle cx="10" cy="10" r="8.5" fill="none" stroke="var(--navy)" stroke-width="1.6"/><path d="M1.5 10h17M10 1.5c-3 3-3 14 0 17M10 1.5c3 3 3 14 0 17M3 5.5h14M3 14.5h14" fill="none" stroke="var(--navy)" stroke-width="1.3"/></svg>
        <span>www.harlowpemberton.com</span>
      </li>
    </ul>
  </section>
</main>
</body>
</html>
```